we need an experienced designer to design the tube for our toothpaste

Design guidelines:
1. On the front side, our product logo (‘K7320’) should be prominent enough.
2. Our brand logo (‘trelvine’) could be small-size and it's just a trademark indeed.

Some information here for your reference:
1. The color of toothpaste cap is white.
2. We hope that the primary color in the design is blue.
3.‘F’ in ‘K7320’ stands for ‘trelvine’ and ‘fluoride’.
4. We will use aluminum-plastic composite materials to make toothpaste tubes. In addition to the design, we also hope that you can make relevant suggestions on the special requirements of printing.

At last, we hope that you could submit both 2D design and 3D visual effects.

Colors
0094D4
00A9DD
6FCCEA
C7EBF8
E9F6FB

Requirements
Must have
• as attached

```html
<!DOCTYPE html>
<html lang="en">
<head>
<meta charset="utf-8">
<title>K7320 Orthodontic Toothpaste – Tube Label</title>
<link rel="stylesheet" href="https://fonts.googleapis.com/css2?family=Fredoka:wght@600&family=Barlow+Condensed:wght@400;500&family=Arimo:ital,wght@0,700;1,700&display=swap">
<style>
  :root {
    --blue: #0094d4;
    --blue-bright: #0096da;
    --blush: #f9cec3;
    --coral: #e0646f;
    --coral-light: #ef7f88;
    --coral-pale: #f7c7c0;
    --ink: #1f1f1f;
    --white: #ffffff;
    --backdrop: #aca5a2;
  }
  * { margin: 0; padding: 0; box-sizing: border-box; }
  html, body { width: 879px; height: 1200px; overflow: hidden; }
  body { background: var(--backdrop); position: relative; font-family: "Arimo", Arial, sans-serif; }

  .label {
    position: absolute;
    left: 19px; top: 331px;
    width: 1046px; height: 670px;
    transform: scale(0.803);
    transform-origin: 0 0;
    background: var(--blush);
    overflow: hidden;
  }
  .label__shapes { position: absolute; inset: 0; }

  .product-type {
    position: absolute; left: 70px; top: 44px;
    font: italic 700 30px "Arimo", Arial, sans-serif;
    color: var(--white); letter-spacing: 0.3px;
  }
  .product-name {
    position: absolute; left: 62px; top: 58px;
    font: 600 190px/1 "Fredoka", "Arial Rounded MT Bold", sans-serif;
    color: var(--white); letter-spacing: -4px;
  }
  .fluoride-tag {
    position: absolute; left: 102px; top: 250px;
    font: italic 700 26px "Arimo", Arial, sans-serif;
    color: var(--white);
  }
  .claim {
    position: absolute; left: 72px; top: 298px;
    font: 700 22.5px/1.2 "Arimo", Arial, sans-serif;
    color: var(--white); letter-spacing: 0.4px;
  }

  .brand {
    position: absolute; left: 822px; top: 58px;
    display: flex; align-items: center; gap: 8px;
    font: 700 30px "Arimo", Arial, sans-serif;
    color: var(--blue);
  }
  .brand__dot { width: 12px; height: 12px; border-radius: 50%; background: var(--blue); }

  .usage {
    position: absolute; right: 105px; top: 150px;
    text-align: right;
    font: 700 21.5px/1.27 "Arimo", Arial, sans-serif;
    color: var(--ink);
  }
  .variant {
    position: absolute; left: 801px; top: 298px;
    font: 700 21.5px/1.27 "Arimo", Arial, sans-serif;
    color: var(--ink); text-align: center;
  }

  .care-title {
    position: absolute; left: 33px; top: 385px; width: 320px;
    text-align: center;
    font: 500 25px/1.22 "Barlow Condensed", "Arial Narrow", sans-serif;
    color: var(--ink);
  }
  .care-art {
    position: absolute; left: 48px; top: 455px;
    width: 290px; height: 78px;
    border-radius: 8px 8px 40px 40px;
    background: linear-gradient(180deg, #ffffff 0%, #f2f2f2 35%, #ee8a93 55%, #e56c78 100%);
  }
  .care-divider {
    position: absolute; left: 36px; top: 535px; width: 320px;
    border-top: 1.5px dashed var(--white);
  }
  .benefits {
    position: absolute; left: 75px; top: 562px;
    width: 233px; list-style: none;
    border: 1.5px solid var(--white); border-radius: 6px;
  }
  .benefits li {
    height: 32px; line-height: 32px; text-align: center;
    font: 700 21px/32px "Arimo", Arial, sans-serif;
    color: var(--ink);
  }
  .benefits li + li { border-top: 1.5px solid var(--white); }

  .info {
    position: absolute; left: 376px; top: 404px; width: 620px;
    font: 400 22.5px/1.35 "Barlow Condensed", "Arial Narrow", sans-serif;
    color: var(--ink);
  }
  .info p + p { margin-top: 13px; }
  .info__key { color: var(--blue); font-weight: 500; }
</style>
</head>
<body>
  <section class="label" aria-label="K7320 orthodontic toothpaste tube label, flat">
    <svg class="label__shapes" viewBox="0 0 1046 670" aria-hidden="true">
      <rect x="0" y="0" width="33" height="670" fill="var(--white)"/>
      <path d="M770 0 H820 C 790 150, 680 330, 430 368 H410 Z" fill="var(--white)"/>
      <path d="M33 0 H770 C 740 130, 640 310, 410 368 H33 Z" fill="var(--blue-bright)"/>
      <rect x="360" y="368" width="686" height="302" fill="var(--white)"/>
      <path d="M348 670 V415 Q350 372 405 368 H430 Q364 380 360 425 V670 Z" fill="var(--blue-bright)"/>
      <polygon points="67,245 380,245 362,289 67,289" fill="var(--coral)"/>
      <polygon points="388,245 470,245 452,289 370,289" fill="var(--coral-light)"/>
      <polygon points="478,245 494,245 476,289 460,289" fill="var(--coral-pale)"/>
      <polygon points="502,245 520,245 502,289 484,289" fill="var(--white)"/>
      <polygon points="528,245 548,245 530,289 510,289" fill="var(--white)"/>
      <circle cx="680" cy="91" r="28" fill="var(--white)"/>
    </svg>

    <p class="product-type">ORTHODONTIC TOOTHPASTE</p>
    <h1 class="product-name">K7320</h1>
    <p class="fluoride-tag">FLUORIDE 1450 PPM</p>
    <p class="claim">ENHANCED CAVITY PREVENTION<br>AND GUM PROTECTION</p>

    <div class="brand"><span>trelvine</span><span class="brand__dot"></span></div>
    <p class="usage">FOR USE WHEN<br>WEARING METAL<br>BRACES AND<br>CLEAR ALIGNERS</p>
    <p class="variant">Double Mint<br>NET WT. 85g</p>

    <h2 class="care-title">PREMIUM ORAL CARE DURING<br>ORTHODONTIC TREATMENT</h2>
    <div class="care-art" role="img" aria-label="Illustration of teeth with metal braces and teeth with clear aligners"></div>
    <div class="care-divider"></div>
    <ul class="benefits">
      <li>Prevent Cavity</li>
      <li>Freshen Breath</li>
      <li>Strengthen Teeth</li>
    </ul>

    <div class="info">
      <p><span class="info__key">Directions:</span> Apply at least one inch strip of the product onto a soft bristle toothbrush. Brush teeth thoroughly, for at least three minutes twice a day.</p>
      <p><span class="info__key">Ingredients:</span> Aqua, Sorbitol, Hydrated Silica, Glycerin, PEG-12, Sodium Lauryl Sulfate, Aroma, Cellulose Gum, Titanium Dioxide, Potassium Sorbate, Allantoin, Sodium Fluoride, Citric Acid, Peppermint Essence, Sodium Saccharin, CI 47005, CI 42090, Cinnamal.</p>
      <p><span class="info__key">Warnings:</span> Do not ingest. Keep out of reach of children under 6 years of age.</p>
    </div>
  </section>
</body>
</html>
```